Kivo Commercial Cleaning is lookong for a new business card design.

A fresh new design that's professional and stylish. We need a serious upgrade to our business cards. I have included pictures of our existing ones. Our clients include professional individuals and business owners. We woupdblike something professional and upbeat. Please have fun and see what you come uo with.

Target Market(s)

Property managers, business owners, facility managers and other similar professionals

Industry/Entity Type

Janitorial

Contact Information for Business Card

Name, cell, office number, email, web address

Font styles to use
Sans Serif

Colors

Designer to choose colors to be used in the design.

Requirements
Must have
• please use the green color in our logo
Nice to have
• Bar code
Should not have
• Address

```html
<!DOCTYPE html>
<html lang="en">
<head>
<meta charset="utf-8">
<title>Kivo Commercial Cleaning – Business Card</title>
<link href="https://fonts.googleapis.com/css2?family=Montserrat:wght@400;500;600;700&display=swap" rel="stylesheet">
<style>
  :root {
    --brand-green: #43ae5a;
    --ink: #2b2b2b;
    --paper: #ffffff;
    --backdrop: #e9e4dc;
  }
  * { margin: 0; padding: 0; box-sizing: border-box; }
  html, body { width: 900px; height: 1200px; overflow: hidden; }
  body {
    background: var(--backdrop);
    font-family: "Montserrat", Arial, sans-serif;
    position: relative;
  }
  .card {
    position: absolute;
    left: 80px;
    width: 742px;
    height: 440px;
    border-radius: 30px;
    overflow: hidden;
  }
  .card-front { top: 132px; background: var(--paper); }
  .card-back { top: 640px; background: var(--brand-green); color: var(--paper); }

  /* front */
  .wordmark-front {
    position: absolute; left: 42px; top: 52px;
    color: var(--brand-green); font-weight: 600; line-height: 1;
  }
  .wordmark-name { display: block; font-size: 86px; letter-spacing: -1px; }
  .wordmark-tag { display: block; font-size: 17px; margin-top: 14px; }

  .holder { position: absolute; left: 42px; top: 272px; }
  .holder-name { color: var(--brand-green); font-size: 26px; font-weight: 700; }
  .holder-title { color: var(--ink); font-size: 15.5px; margin-top: 2px; }

  .rule { position: absolute; left: 42px; top: 330px; width: 653px; height: 2px; background: var(--brand-green); }

  .contacts { position: absolute; left: 42px; top: 342px; list-style: none; }
  .contacts li {
    display: flex; align-items: center; gap: 11px;
    color: var(--ink); font-size: 16px; height: 22.5px;
  }
  .contacts svg { width: 13px; height: 13px; fill: var(--brand-green); }

  /* back */
  .wordmark-back {
    position: absolute; left: 60px; top: 160px; width: 330px;
    text-align: center; font-weight: 600; line-height: 1;
  }
  .wordmark-back .wordmark-name { font-size: 104px; }
  .wordmark-back .wordmark-tag { font-size: 20px; margin-top: 18px; }

  .divider { position: absolute; left: 408px; top: 145px; width: 2px; height: 182px; background: var(--paper); }

  .services { position: absolute; left: 456px; top: 140px; }
  .services-title { font-size: 19px; font-weight: 600; margin-bottom: 6px; }
  .services-list { list-style: none; }
  .services-list li { font-size: 16px; height: 19.7px; line-height: 19.7px; padding-left: 14px; position: relative; }
  .services-list li::before {
    content: ""; position: absolute; left: 0; top: 8px;
    width: 6px; height: 6px; border-radius: 50%; background: var(--paper);
  }
</style>
</head>
<body>

<section class="card card-front">
  <div class="wordmark-front">
    <span class="wordmark-name">Kivo</span>
    <span class="wordmark-tag">Kivo Commercial Cleaning</span>
  </div>

  <div class="holder">
    <h1 class="holder-name">Dana Whitfield</h1>
    <p class="holder-title">CEO &amp; Founder</p>
  </div>

  <div class="rule"></div>

  <ul class="contacts">
    <li>
      <svg viewBox="0 0 16 16" aria-hidden="true"><path d="M2 6c0-2 2.5-3 6-3s6 1 6 3v1h-3.5V5.5h-5V7H2z"/><path d="M3 9l2-2h6l2 2v4H3z"/></svg>
      (37) 555-0182
    </li>
    <li>
      <svg viewBox="0 0 16 16" aria-hidden="true"><path d="M1 3h14v1.2L8 8.8 1 4.2z"/><path d="M1 5.8l7 4.6 7-4.6V13H1z"/></svg>
      dana@kivocleaning.com
    </li>
    <li>
      <svg viewBox="0 0 16 16" aria-hidden="true"><circle cx="8" cy="8" r="7"/><path d="M5 4.5c1.5.5 2 1.5 1 2.5s.5 2 2 1.5 1 2 0 3.5" stroke="#fff" stroke-width="1.3" fill="none"/></svg>
      www.kivocleaning.com
    </li>
  </ul>
</section>

<section class="card card-back">
  <div class="wordmark-back">
    <span class="wordmark-name">Kivo</span>
    <span class="wordmark-tag">Kivo Commercial Cleaning</span>
  </div>

  <div class="divider"></div>

  <div class="services">
    <h2 class="services-title">OUR SERVICES</h2>
    <ul class="services-list">
      <li>Carpet Cleaning</li>
      <li>Construction Cleaning</li>
      <li>Day Labor</li>
      <li>Furniture Cleaning</li>
      <li>Power Washing</li>
      <li>VCT Cleaning</li>
      <li>Window Cleaning</li>
      <li>Furniture Cleaning</li>
    </ul>
  </div>
</section>

</body>
</html>
```